依頼詳細
A4サイズカラー両面チラシのデザイン
・光触媒コーティングサービスのメリットが伝わるもの
・イラストを使用して、わかりやすいもの
※チラシデザインを決定させていただき、それをベースにLPデザインも追加依頼予定(別途料金)
記載項目
株式会社Sorano Works
山口県山口市小郡若葉町3-17
TEL 083-512-4937
サイズ
A4
ページ数
両面
希望イメージ
シンプル 複雑
単色 カラフル
暗い 明るい
日常 高級
遊び心 厳粛
未来的 伝統的
女性的 男性的
希望する色
黄・オレンジ系、緑系、青系
納品ファイル
• イラストレーター形式 (.ai)
■ 選んだ理由

完成イメージに近かったです。

■ 提案者全員のお礼・コメント

皆様、ご提案ありがとうございました。

```html
<!DOCTYPE html>
<html lang="ja">
<head>
<meta charset="UTF-8">
<title>光触媒コーティング 脱臭・除菌対策チラシ</title>
<link rel="stylesheet" href="https://fonts.googleapis.com/css2?family=Noto+Sans+JP:wght@400;500;700;900&display=swap">
<style>
:root{
  --yellow:#ffe600;
  --red:#e60012;
  --green:#3a9e3a;
  --ink:#1a1a1a;
  --white:#ffffff;
  --grey:#6b6b6b;
  --line:#c9c9c9;
  --orange:#f39800;
  --blue:#2b8fd6;
}
*{margin:0;padding:0;box-sizing:border-box}
html,body{width:849px;height:1200px;overflow:hidden}
body{font-family:"Noto Sans JP",sans-serif;color:var(--ink);background:var(--white)}
.flyer{position:relative;width:849px;height:1200px;background:var(--yellow);overflow:hidden}
.abs{position:absolute}

.venues{left:34px;top:30px;width:781px;display:flex;gap:8px}
.venues li{list-style:none;flex:1;background:var(--green);color:var(--white);font-weight:700;font-size:15px;text-align:center;padding:5px 0;letter-spacing:.02em}

.product-name{left:42px;top:82px;width:300px;height:44px;background:var(--white);font-size:15px;font-weight:500;padding:11px 16px}

.headline{left:38px;top:132px;display:flex;align-items:flex-end;color:var(--red);font-weight:900;line-height:1}
.headline .label{writing-mode:vertical-rl;font-size:26px;letter-spacing:.05em;margin-right:6px;margin-bottom:6px}
.headline .rate{font-size:118px;letter-spacing:-.02em}
.headline .rate small{font-size:84px}
.headline .verb{font-size:92px;margin-left:4px;margin-bottom:2px}

.viruses{left:610px;top:90px;width:210px;height:190px;border-radius:50%;background:radial-gradient(circle at 50% 50%,#f08a3c 0%,#e8503a 55%,rgba(230,0,18,0) 72%)}

.proof{left:44px;top:252px;font-size:26px;font-weight:700;letter-spacing:.01em}

.title{left:34px;top:270px;display:flex;align-items:flex-end;font-weight:900;line-height:1}
.title .main{font-size:150px;letter-spacing:-.03em}
.title .sub{font-size:50px;color:var(--red);writing-mode:vertical-rl;margin-left:6px;margin-bottom:16px}

.benefits{left:28px;top:438px;width:793px;height:250px;background:var(--white)}
.coating{position:absolute;left:26px;top:14px;display:flex;align-items:flex-end;gap:10px}
.coating h2{font-size:56px;font-weight:900;color:var(--red);line-height:1;border-bottom:4px solid var(--red);padding-bottom:4px}
.coating p{font-size:24px;font-weight:700;padding-bottom:10px}
.keys{position:absolute;left:26px;top:94px;display:flex;align-items:center;gap:14px}
.keys .key{border:3px solid var(--ink);font-size:34px;font-weight:900;padding:4px 14px;line-height:1.2}
.keys .plus{font-size:44px;font-weight:900}
.points{position:absolute;left:26px;top:170px;width:741px;display:flex;gap:10px}
.points li{list-style:none;flex:1;background:#fff4b0;border:1px solid var(--orange);font-size:13px;font-weight:500;line-height:1.6;padding:10px 8px;text-align:center;white-space:nowrap}

.mechanism{left:28px;top:706px;width:793px;height:370px;background:var(--white);border:2px solid var(--line)}
.mechanism .tab{position:absolute;left:50%;top:-2px;transform:translateX(-50%);background:var(--green);color:var(--white);font-weight:700;font-size:18px;padding:4px 34px}
.spray{position:absolute;left:14px;top:60px;width:190px}
.spray .art{height:180px;border-radius:8px;background:linear-gradient(160deg,#dff0ff,#b9d9f2)}
.spray p{font-size:13px;font-weight:700;line-height:1.4;margin-top:8px}
.spray p strong{display:block;font-size:20px;font-weight:900;color:var(--ink)}
.surface{position:absolute;left:215px;top:44px;width:300px;height:310px;border-radius:8px;background:linear-gradient(180deg,#fff7c9 0%,#e7f4ff 55%,#cfe6c6 100%)}
.surface .tag{position:absolute;background:var(--ink);color:var(--white);font-size:15px;font-weight:700;padding:6px 8px;border-radius:50%;width:60px;height:60px;display:flex;align-items:center;justify-content:center;text-align:center;line-height:1.1}
.surface .sun{position:absolute;left:150px;top:14px;font-size:13px;font-weight:700}
.effects{position:absolute;left:540px;top:44px;width:150px;display:grid;grid-template-columns:1fr 1fr;gap:8px}
.effects span{width:68px;height:68px;border-radius:50%;background:var(--blue);color:var(--white);font-weight:700;font-size:18px;display:flex;align-items:center;justify-content:center}
.effects span:nth-child(5){grid-column:1 / span 2;justify-self:center}
.staff{position:absolute;left:700px;top:40px;width:80px;height:236px;border-radius:8px;background:linear-gradient(180deg,#efe6dc,#c9c3bd)}
.bubble{position:absolute;left:604px;top:248px;background:var(--white);border:2px solid var(--ink);border-radius:14px;font-size:11px;font-weight:700;padding:4px 10px;white-space:nowrap}
.targets{position:absolute;left:536px;top:290px;width:238px;font-size:11px;line-height:1.5;color:var(--grey)}

.offer{left:28px;top:1090px;width:793px;height:92px;display:flex;align-items:center}
.offer .lead{font-size:17px;font-weight:700;line-height:1.35}
.offer .lead strong{display:block;font-size:30px;font-weight:900;color:var(--red)}
.offer .time{margin-left:22px;border:2px solid var(--ink);background:var(--white);padding:6px 10px;display:flex;align-items:center;gap:8px;font-size:13px;font-weight:700;line-height:1.2}
.offer .time b{font-size:22px}
.offer .price{margin-left:auto;display:flex;align-items:center;gap:8px;font-weight:900;color:var(--red)}
.offer .price svg{width:40px;height:30px}
.offer .price span{font-size:58px;letter-spacing:-.01em}
.offer .price small{font-size:30px}
</style>
</head>
<body>
<div class="flyer">
  <ul class="venues abs">
    <li>幼稚園</li><li>保育園</li><li>高齢者施設</li><li>整体院</li><li>美容室</li><li>飲食店</li><li>オフィス</li><li>住宅</li>
  </ul>

  <div class="product-name abs">商品名が入ります</div>

  <div class="headline abs">
    <span class="label">ウィルス</span>
    <span class="rate">99.9<small>%</small></span>
    <span class="verb">減少</span>
  </div>
  <div class="viruses abs" role="img" aria-label="赤とオレンジのウィルスのイラスト"></div>

  <p class="proof abs">公的機関で実証済み（A型インフルエンザウィルス）</p>

  <div class="title abs">
    <span class="main">脱臭･除菌</span>
    <span class="sub">対策</span>
  </div>

  <section class="benefits abs">
    <div class="coating">
      <h2>光触媒コーティング</h2>
      <p>一度の噴霧だけで</p>
    </div>
    <div class="keys">
      <span class="key">長期間抗菌</span>
      <span class="plus">＋</span>
      <span class="key">ウィルスを分解・不活性化</span>
    </div>
    <ul class="points">
      <li>都度のアルコール消毒は<br>必要なし</li>
      <li>一度噴霧すれば<br>効果は数年持続</li>
      <li>ドアノブ・防汚性能で<br>さっと水拭きだけ、お手入れが楽に</li>
    </ul>
  </section>

  <section class="mechanism abs">
    <div class="tab">光触媒のしくみ</div>
    <div class="spray">
      <div class="art" role="img" aria-label="スプレーで光触媒を噴霧する作業員のイラスト"></div>
      <p>光触媒<br>超微粒子酸化チタンを使った<strong>光触媒コーティング</strong></p>
    </div>
    <div class="surface" role="img" aria-label="光に反応して壁面の菌が消滅するしくみの図">
      <span class="sun">太陽　蛍光灯など</span>
      <span class="tag" style="left:14px;top:20px">菌が<br>消滅</span>
      <span class="tag" style="left:220px;top:236px">菌が<br>消滅</span>
    </div>
    <div class="effects">
      <span>抗菌</span><span>除菌</span><span>防臭</span><span>防カビ</span><span>防汚</span>
    </div>
    <div class="staff" role="img" aria-label="案内する女性スタッフの写真"></div>
    <span class="bubble">お気軽にご相談ください</span>
    <p class="targets">インフルエンザウィルス、ノロウイルス、大腸菌、カビ、生活臭などに幅広く効果を発揮します。</p>
  </section>

  <div class="offer abs">
    <p class="lead">革新的な抗菌&amp;除菌で<strong>低価格化を実現</strong></p>
    <div class="time">
      <b>6㎡</b>
      <span>/時間<br>（施工目安）</span>
    </div>
    <div class="price">
      <svg viewBox="0 0 40 30" aria-hidden="true"><path d="M0 10h24V2l16 13-16 13v-8H0z" fill="#e60012"/></svg>
      <span>39,000<small>円〜</small></span>
    </div>
  </div>
</div>
</body>
</html>
```